Stationary/Biz Card for Small Business Coaches
Bramblecrest Advisory Circle
Professional
Martin Kalbrun
President
418 Fenwick Lane
Harlan, IA 50294
mkalbrun@bramblecrestadvisory.example
www.bramblecrestadvisory.example
Tag line: Walking With Leaders to Achieve Growth

```html
<!DOCTYPE html>
<html lang="en">
<head>
<meta charset="utf-8">
<title>Bramblecrest Advisory Circle – Stationery</title>
<link href="https://fonts.googleapis.com/css2?family=Lato:wght@400;700&display=swap" rel="stylesheet">
<style>
:root{
  --navy:#1f3c8f;
  --orange:#e2693a;
  --paper:#ffffff;
  --ground:#e9e4dc;
  --ink:#4a4a4a;
  --faint:#dfe3ee;
  --label:#6b655c;
}
*{margin:0;padding:0;box-sizing:border-box}
html,body{width:1200px;height:446px;overflow:hidden}
body{background:var(--ground);font-family:"Lato",sans-serif;position:relative}
.piece{position:absolute;background:var(--paper);box-shadow:0 2px 5px rgba(0,0,0,.18)}
.label{position:absolute;font-size:8px;letter-spacing:.6px;color:var(--label);text-transform:uppercase}
.brand{display:flex;align-items:center;gap:4px;color:var(--navy);font-weight:700;white-space:nowrap}
.brand .dot{width:8px;height:8px;border-radius:50%;background:var(--orange);flex:none}
.tagline{font-size:4px;color:var(--ink);letter-spacing:.3px}

/* business card */
.card{left:19px;top:211px;width:130px;height:72px;padding:8px;border-left:5px solid var(--navy)}
.card .brand{font-size:7px}
.card .person{margin-top:10px;font-size:6px;color:var(--navy);font-weight:700}
.card .details{font-size:4.5px;color:var(--ink);line-height:1.45;margin-top:2px}

/* letterheads */
.letterhead{top:19px;width:298px;height:396px;border:4px solid var(--navy);padding:14px 22px}
.letterhead .brand{font-size:9px}
.letterhead .contact{position:absolute;font-size:4.5px;line-height:1.5;color:var(--ink)}
.lh-one{left:163px}
.lh-one .contact{top:16px;right:40px}
.lh-one .watermark{position:absolute;left:20px;right:20px;bottom:40px;text-align:center}
.lh-two{left:475px}
.lh-two .brand{justify-content:center}
.lh-two .tagline{text-align:center;margin-top:2px}
.lh-two .contact{left:0;right:0;bottom:14px;text-align:center}
.lh-two .watermark{position:absolute;left:20px;right:20px;top:150px;text-align:center}
.watermark{font-size:22px;font-weight:700;color:var(--faint);line-height:1.1}

/* envelopes */
.envelope{left:792px;width:396px}
.env-back{top:19px;height:65px}
.env-orange{top:96px;height:132px;background:var(--orange);overflow:hidden}
.env-orange .flap{position:absolute;left:0;top:0;width:100%;height:70px}
.env-orange .brand{position:absolute;left:50%;top:14px;transform:translateX(-50%);color:var(--paper);font-size:9px}
.env-orange .brand .dot{background:var(--paper)}
.env-white{top:216px;height:96px}
.env-white .flap{position:absolute;left:0;top:0;width:100%;height:60px}
.env-white .brand{position:absolute;left:50%;top:12px;transform:translateX(-50%);font-size:9px}
.env-front{top:336px;height:68px;border:5px solid var(--navy);padding:8px 12px}
.env-front .brand{font-size:8px}
.env-front .details{font-size:4.5px;color:var(--ink);line-height:1.4;margin-top:2px}
</style>
</head>
<body>

<div class="label" style="left:19px;top:196px">Business Cards</div>
<div class="piece card">
  <div class="brand"><span class="dot"></span>Bramblecrest Advisory Circle</div>
  <div class="person">Martin Kalbrun · President</div>
  <div class="details">418 Fenwick Lane, Harlan, IA 50294<br>mkalbrun@bramblecrestadvisory.example<br>www.bramblecrestadvisory.example</div>
</div>

<div class="piece letterhead lh-one">
  <div class="brand"><span class="dot"></span>Bramblecrest Advisory Circle</div>
  <div class="tagline">Walking With Leaders to Achieve Growth</div>
  <div class="contact">418 Fenwick Lane<br>Harlan, IA 50294<br>mkalbrun@bramblecrestadvisory.example<br>www.bramblecrestadvisory.example</div>
  <div class="watermark">Bramblecrest<br>Advisory Circle</div>
</div>
<div class="label" style="left:270px;top:424px">Letterhead Option 1</div>

<div class="piece letterhead lh-two">
  <div class="brand"><span class="dot"></span>Bramblecrest Advisory Circle</div>
  <div class="tagline">Walking With Leaders to Achieve Growth</div>
  <div class="watermark">Bramblecrest<br>Advisory Circle</div>
  <div class="contact">418 Fenwick Lane, Harlan, IA 50294 · mkalbrun@bramblecrestadvisory.example · www.bramblecrestadvisory.example</div>
</div>
<div class="label" style="left:582px;top:424px">Letterhead Option 2</div>

<div class="piece envelope env-back"></div>

<div class="piece envelope env-orange">
  <svg class="flap" viewBox="0 0 396 70" preserveAspectRatio="none"><path d="M0 0H396L198 70Z" fill="#ffffff"/></svg>
  <div class="brand"><span class="dot"></span>Bramblecrest Advisory Circle</div>
</div>

<div class="piece envelope env-white">
  <svg class="flap" viewBox="0 0 396 60" preserveAspectRatio="none"><path d="M0 0L198 60L396 0" fill="none" stroke="#d8d8d8" stroke-width="1"/></svg>
  <div class="brand"><span class="dot"></span>Bramblecrest Advisory Circle</div>
</div>

<div class="piece envelope env-front">
  <div class="brand"><span class="dot"></span>Bramblecrest Advisory Circle</div>
  <div class="details">418 Fenwick Lane<br>Harlan, IA 50294</div>
</div>
<div class="label" style="left:945px;top:412px">Envelope Option 1</div>

</body>
</html>
```